Coralbend Pastoral Traders Business Cards

We require business cards revamped with our logo. A few details we would like to use.

1. Round Edges
2. Our logo over the top of a wagyu cattle background photo on one side of the card

Other side of the card has the below details.

1. Person Name (First & Last)
2. Job Position
3. Mobile Number
4. Email Address
5. Website Address

Simple & Neat.

Target Market(s)

Sales

Industry/Entity Type

Agriculture

Contact Information for Business Card

CORALBEND PASTORAL TRADERS

Colors

Designer to choose colors to be used in the design.

Requirements
Must have
• Company Logo

```html
<!DOCTYPE html>
<html lang="en">
<head>
<meta charset="utf-8">
<title>Coralbend Pastoral Traders – Business Cards</title>
<link rel="stylesheet" href="https://fonts.googleapis.com/css2?family=Rubik:wght@400;500;700&display=swap">
<style>
  :root {
    --backdrop: #5b1b1d;
    --brand-red: #b0121a;
    --brand-red-deep: #7c0c12;
    --ink: #2b2b2b;
    --ink-soft: #7a7a7a;
    --paper: #ffffff;
    --photo-dark: #2a2c29;
    --photo-mid: #3b3d36;
  }
  * { box-sizing: border-box; margin: 0; padding: 0; }
  html, body {
    width: 1200px; height: 1200px; overflow: hidden;
    background: var(--backdrop);
    font-family: "Rubik", Arial, sans-serif;
  }
  .canvas {
    width: 1200px; height: 1200px;
    display: flex; flex-direction: column; align-items: center; justify-content: center;
    gap: 56px;
  }
  .card {
    position: relative;
    width: 900px; height: 514px;
    border-radius: 34px;
    overflow: hidden;
    box-shadow: 0 18px 40px rgba(0,0,0,.35);
  }

  /* Front */
  .card-front { background: var(--photo-dark); }
  .cattle-photo {
    position: absolute; inset: 0;
    background:
      radial-gradient(ellipse 45% 55% at 55% 45%, #1c1c1a 0%, transparent 70%),
      linear-gradient(180deg, #3a3d3b 0%, var(--photo-mid) 45%, #4a4533 75%, #2d2b24 100%);
  }
  .front-halftone {
    position: absolute; left: 0; right: 0; bottom: 0; height: 170px;
    background: linear-gradient(180deg, rgba(176,18,26,0) 0%, rgba(176,18,26,.45) 55%, rgba(124,12,18,.85) 100%);
  }
  .front-logo {
    position: absolute; left: 50%; top: 50%;
    transform: translate(-50%, -50%);
    display: flex; align-items: center; gap: 16px;
  }
  .logo-mark {
    width: 30px; height: 30px; border-radius: 50%;
    background: var(--brand-red); flex: none;
  }
  .front-logo .logo-name {
    color: var(--brand-red);
    font-weight: 700; font-size: 40px; letter-spacing: 1px;
    white-space: nowrap;
  }

  /* Back */
  .card-back { background: var(--paper); }
  .back-accent { position: absolute; right: 0; top: 0; width: 320px; height: 514px; }
  .back-halftone {
    position: absolute; right: 0; bottom: 0; width: 300px; height: 300px;
    background: radial-gradient(circle at 100% 70%, rgba(176,18,26,.75) 0%, rgba(176,18,26,.25) 45%, rgba(176,18,26,0) 70%);
  }
  .holder {
    position: absolute; right: 150px; top: 44px; text-align: right;
  }
  .holder-name { font-size: 30px; color: var(--ink-soft); font-weight: 400; line-height: 1.2; }
  .holder-name strong { color: var(--brand-red); font-weight: 700; }
  .holder-title { font-size: 17px; color: var(--ink-soft); margin-top: 4px; }
  .holder-tagline {
    margin-top: 10px; font-size: 16px; color: var(--brand-red); line-height: 1.3;
  }
  .back-logo {
    position: absolute; left: 50px; top: 176px;
    display: flex; align-items: center; gap: 12px;
  }
  .back-logo .logo-mark { width: 24px; height: 24px; }
  .back-logo .logo-name {
    color: var(--brand-red); font-weight: 700; font-size: 24px; letter-spacing: .5px; white-space: nowrap;
  }
  .address {
    position: absolute; left: 90px; top: 250px;
    font-size: 20px; color: var(--ink); line-height: 1.45; font-style: normal;
  }
  .contacts {
    position: absolute; left: 90px; top: 350px;
    list-style: none; font-size: 20px; color: var(--ink);
  }
  .contacts li { display: flex; align-items: center; gap: 14px; height: 36px; }
  .contacts svg { width: 20px; height: 20px; flex: none; }
</style>
</head>
<body>
<main class="canvas">

  <section class="card card-front">
    <div class="cattle-photo" role="img" aria-label="Photograph of a black wagyu bull standing in dry grassland"></div>
    <div class="front-halftone" role="img" aria-label="Red halftone dot pattern fading up from the bottom edge"></div>
    <div class="front-logo">
      <span class="logo-mark"></span>
      <span class="logo-name">CORALBEND PASTORAL TRADERS</span>
    </div>
  </section>

  <section class="card card-back">
    <svg class="back-accent" viewBox="0 0 320 514" aria-hidden="true">
      <path d="M270 0 H320 V210 C312 160 300 120 270 90 C250 70 240 40 270 0 Z" fill="var(--brand-red)"/>
    </svg>
    <div class="back-halftone" role="img" aria-label="Red halftone dot pattern in the lower right corner"></div>

    <div class="holder">
      <p class="holder-name"><strong>Marcus</strong> Hollway</p>
      <p class="holder-title">Beef Export owners</p>
      <p class="holder-tagline">We are a trusted exporter of wagyu meat<br>with the best quality meat.</p>
    </div>

    <div class="back-logo">
      <span class="logo-mark"></span>
      <span class="logo-name">CORALBEND PASTORAL TRADERS</span>
    </div>

    <address class="address">
      48 Saltbush Run<br>Coralbend QLD 4870
    </address>

    <ul class="contacts">
      <li>
        <svg viewBox="0 0 24 24" fill="none" stroke="var(--ink)" stroke-width="1.6"><path d="M6 3h3l2 5-2.5 1.5a11 11 0 0 0 6 6L16 13l5 2v3a2 2 0 0 1-2 2A16 16 0 0 1 4 5a2 2 0 0 1 2-2z"/></svg>
        <span>+61-4720-3391</span>
      </li>
      <li>
        <svg viewBox="0 0 24 24" fill="none" stroke="var(--ink)" stroke-width="1.6"><rect x="3" y="5" width="18" height="14" rx="1"/><path d="M3 6l9 7 9-7"/></svg>
        <span>hello@coralbendpastoral.au</span>
      </li>
      <li>
        <svg viewBox="0 0 24 24" fill="none" stroke="var(--ink)" stroke-width="1.6"><circle cx="12" cy="12" r="9"/><path d="M3 12h18M12 3c3 3 3 15 0 18M12 3c-3 3-3 15 0 18"/></svg>
        <span>www.coralbendpastoral.au</span>
      </li>
    </ul>
  </section>

</main>
</body>
</html>
```